Ecommerce Website

Hello designers of Pixel Bazaar,

Today I'm requesting webpage designs for my new start up business in Toronto Canada. I have little or no experience in this field so I decided to outsource it here! My business revolves around the retail of customizable smartphone cases, as well as other objects such as mouse pads, mugs, etc.. Our main focus is smartphone cases, tablets and such. There are a few of these types of websites out already so the idea shouldn't be too foreign. I am looking for a minimalist look for my website revolving around light colours. Should convey a sense of simplistic design with elegant feel while including aspects of the business. Please see current website at brightcasewerk.ca to see how the set-up is (currently on pre-made template). Should have a similar feel to it. Also i have a post for logo design as i currently do not have one. If you can create a logo as well for my other post along with this one, gives preference to artist.

http://jobs.pixelbazaar.com/job.aspx?id=987612
Updates

The design should be transferable to the other webpages on the site. The overall look should be the same (borders, buttons, etc)

I am not sure if I'm allowed to request the page in coding as it said non-coded earlier. However it would be preferable to have the website in CSS or HTML as well as a PSD version for alterations.

Wasn't too clear about the total requirements. We are looking for a main homepage as well as a general design for the rest of our pages such as browsing catalogue page, product page, etc.. Should be a general look that can be used for multiple pages.

I have committed the payment so please do not hesitate to post designs.

To All designers.  I have attached the logo to the brief. It has multiple colors which you can choose from. The last one on the second row is the one i prefer the best however if your site can match well with any other ones, that is okay as well. 

Reason: have a few designs for selection in mind however need to get it to the final point.

Target Market(s)

Young adults ages 19 - 32

Industry/Entity Type

Retail

Requirements
Must have
• Main slider design - Main page will have a slider which displays new products or services. Please see brightcasewerk.ca for example

Note worthy - Currently we are using a service from http://www.printlumo.com/ so please make sure that it the design will work with that in mind.

```html
<!DOCTYPE html>
<html lang="en">
<head>
<meta charset="utf-8">
<title>Brightcase Werk – Custom Cases</title>
<link href="https://fonts.googleapis.com/css2?family=Arimo:wght@400;700&family=Open+Sans:wght@300;400;700&display=swap" rel="stylesheet">
<style>
:root{
  --green:#7cb342;
  --green-dark:#5f9a2c;
  --blue:#1e8fd0;
  --blue-dark:#0b6fb0;
  --teal:#1aa3c8;
  --link:#2a7bb4;
  --text:#444;
  --muted:#666;
  --panel:#f0f0f0;
  --dark:#333;
  --darker:#2a2a2a;
  --price:#c0221a;
  --footer-head:#3fb9e6;
}
*{box-sizing:border-box;margin:0;padding:0}
html,body{width:920px;height:1200px;overflow:hidden}
body{position:relative;background:#fff;font-family:Arimo,Arial,sans-serif;color:var(--text);font-size:11px}
.abs{position:absolute}

/* top bar */
.topbar{left:0;top:0;width:920px;height:43px;background:linear-gradient(#3c3c3c,#555)}
.top-btn{top:10px;height:22px;background:linear-gradient(#7cc24a,#58a22b);color:#fff;font-size:11px;font-weight:700;line-height:22px;text-align:center;border:1px solid #4d8d25}
.search{left:722px;top:10px;width:130px;height:22px;background:#fff;border:1px solid #ccc;font-size:9px;line-height:20px;padding-left:10px;color:#333}
.search svg{position:absolute;right:7px;top:4px}

/* header */
.header{left:0;top:43px;width:920px;height:133px;background:linear-gradient(90deg,#f2f2f2,#fff 40%,#f6f6f6)}
.brand{left:69px;top:62px;display:flex;align-items:center;gap:10px}
.brand-mark{width:40px;height:40px;background:var(--blue)}
.brand-name{font-family:Arimo,Arial,sans-serif;font-weight:700;font-size:30px;line-height:30px;color:var(--green);letter-spacing:1px}
.cart{left:604px;top:57px;width:248px;height:62px;background:#fff;border-radius:4px;box-shadow:0 0 3px rgba(0,0,0,.08)}
.cart-icon{left:0;top:0;width:73px;height:62px;border-right:1px solid #e4e4e4;text-align:center;font-size:10px;color:#444}
.cart-icon svg{margin:8px auto 2px;display:block}
.cart-info{left:88px;top:8px;font-size:10px;line-height:17.5px;color:#333}
.currency{left:169px;top:28px;width:66px;height:22px;border:1px solid #ccc;font-size:9px;line-height:20px;padding-left:24px;color:#333}
.currency .flag{position:absolute;left:7px;top:6px;width:12px;height:8px;background:#2b4a8a}
.currency .caret{position:absolute;right:8px;top:9px;border:3px solid transparent;border-top:4px solid #333}

/* nav */
.navband{left:0;top:172px;width:920px;height:4px;background:var(--blue)}
.nav{left:69px;top:134px;width:783px;height:42px;display:flex;background:linear-gradient(#27a0e0,var(--blue-dark));border-radius:3px 3px 0 0;overflow:hidden}
.nav a{color:#fff;text-decoration:none;font-weight:700;font-size:11.5px;line-height:42px;text-align:center;border-right:1px solid rgba(0,0,0,.18);text-shadow:0 1px 1px rgba(0,0,0,.3)}
.nav a.active{background:linear-gradient(#8a8a8a,#5a5a5a)}

/* slider */
.slider{left:0;top:176px;width:920px;height:232px;background:radial-gradient(ellipse 70% 60% at 50% 110%,#fff 60%,#e4e4e4 100%),#e8e8e8}
.slide-photo{left:78px;top:204px;width:250px;height:188px;background:linear-gradient(135deg,#2b2b2b,#4a4a4a 55%,#8a8a9a);border-radius:8px}
.slide-panel{left:332px;top:210px;width:506px;height:147px;background:#fff;border-radius:6px}
.slide-title{left:359px;top:220px;font-family:"Open Sans",sans-serif;font-weight:300;font-size:29px;color:var(--teal)}
.slide-text{left:359px;top:258px;width:336px;font-size:10.3px;line-height:16px;color:#444}
.dark-btn{height:30px;background:linear-gradient(#6a6a6a,#3c3c3c);border-radius:3px;color:#fff;font-weight:700;font-size:11.5px;line-height:30px;padding-left:13px;border:1px solid #2c2c2c}
.dark-btn .chev{position:absolute;right:14px;top:8px;width:12px;height:12px;border-radius:50%;background:#2a2a2a}
.dark-btn .chev::after{content:"";position:absolute;left:3px;top:4px;width:3px;height:3px;border-top:1.5px solid #fff;border-right:1.5px solid #fff;transform:rotate(45deg)}
.price-badge{left:709px;top:225px;width:118px;height:118px;border-radius:50%;background:var(--teal);color:#fff;text-align:center;font-family:"Open Sans",sans-serif}
.price-badge .just{display:block;margin-top:20px;font-weight:300;font-size:25px;line-height:28px}
.price-badge .amt{display:block;font-weight:700;font-size:28px;line-height:34px}
.dot{top:375px;width:14px;height:14px;border-radius:50%;background:#777}
.dot.on{background:var(--blue)}

/* section headings */
.section-head{height:34px;background:var(--green);color:#fff;font-weight:700;font-size:14px;line-height:34px;padding-left:11px}
.section-head .go{position:absolute;right:12px;top:10px;width:14px;height:14px;border-radius:50%;background:#3f7b17}
.section-head .go::after{content:"";position:absolute;left:3px;top:4.5px;width:3px;height:3px;border-top:1.5px solid #fff;border-right:1.5px solid #fff;transform:rotate(45deg)}

/* products */
.product{top:488px;width:160px;height:218px;background:var(--panel)}
.product .shot{position:absolute;left:5px;top:4px;width:151px;height:110px;background:#fff}
.product .shot i{position:absolute;left:28px;top:18px;width:95px;height:74px;border-radius:8px;background:linear-gradient(135deg,#3a3a3a,#777 60%,#bbb)}
.product .name{position:absolute;left:12px;top:126px;width:140px;color:var(--link);font-size:11.5px;line-height:14px}
.product .price{position:absolute;left:12px;color:#444;font-size:10.5px}
.product .price b{font-weight:400;color:var(--price)}
.cart-btn{position:absolute;left:11px;top:180px;width:139px;height:27px;background:linear-gradient(#5a5a5a,#2e2e2e);border-radius:3px;color:#fff;font-size:11.5px;line-height:27px;padding-left:44px}
.cart-btn svg{position:absolute;left:18px;top:6px}

/* create new */
.intro{left:81px;top:776px;width:516px;font-size:10.4px;line-height:17.6px;color:#444;text-align:justify}
.create-card{top:878px;width:245px;height:75px;border:1px solid #e0e0e0;background:linear-gradient(90deg,#fff,#f0f0f0)}
.create-card .thumb{position:absolute;left:22px;top:6px;width:50px;height:64px;border-radius:4px;background:linear-gradient(135deg,#222,#555 50%,#c33)}
.create-card .label{position:absolute;left:95px;top:14px;font-weight:700;font-size:15px;line-height:24px;color:#666}

/* categories */
.cat-panel{left:625px;top:474px;width:227px;height:495px;background:#f5f5f5}
.cat-list{list-style:none;position:absolute;left:20px;top:14px}
.cat-list li{font-size:12px;line-height:24px;color:var(--link);padding-left:16px;position:relative}
.cat-list li::before{content:"";position:absolute;left:0;top:10px;border:2.5px solid transparent;border-left:3px solid var(--link)}

/* footer */
.footer{left:0;top:975px;width:920px;height:187px;background:var(--dark);border-top:3px solid #222}
.foot-head{color:var(--footer-head);font-size:13.5px}
.foot-list{list-style:none;font-size:10px;color:#ddd}
.foot-list li{line-height:22.4px;padding-left:9px;position:relative}
.foot-list li::before{content:"";position:absolute;left:0;top:10px;width:3px;height:3px;border-radius:50%;background:#ddd}
.vdiv{top:992px;width:1px;height:158px;background:#555}
.field{left:486px;width:174px;height:22px;background:#fff;border:1px solid #bbb;font-size:8.5px;line-height:20px;padding-left:12px;color:#333}
.submit{left:606px;top:1092px;width:54px;height:22px;background:linear-gradient(#37c2ee,#1a9ed0);color:#fff;font-weight:700;font-size:11px;line-height:22px;text-align:center}
.social{left:694px;display:flex;align-items:center;font-size:9.5px;color:#ddd}
.social .sq{width:20px;height:20px;background:#3b67b0;margin-right:18px;border:1px solid #777}
.social b{font-weight:400;font-size:11px;color:var(--footer-head);margin-left:5px}
.copyright{left:0;top:1162px;width:920px;height:38px;background:var(--darker);color:#aaa;font-size:9.5px;line-height:38px;text-align:center}
</style>
</head>
<body>

<div class="abs topbar"></div>
<div class="abs top-btn" style="left:605px;width:53px">LOG IN</div>
<div class="abs top-btn" style="left:662px;width:57px">SIGN UP</div>
<div class="abs search">Search
  <svg width="13" height="13" viewBox="0 0 13 13"><circle cx="5" cy="5" r="3.6" fill="none" stroke="#222" stroke-width="2"/><line x1="7.5" y1="7.5" x2="12" y2="12" stroke="#222" stroke-width="2.4"/></svg>
</div>

<div class="abs header"></div>
<div class="abs brand"><span class="brand-mark"></span><span class="brand-name">BRIGHTCASE<br>WERK</span></div>

<div class="abs cart">
  <div class="abs cart-icon">
    <svg width="30" height="26" viewBox="0 0 30 26"><path d="M3 10h24l-3 14H6z" fill="none" stroke="#888" stroke-width="2"/><path d="M8 10l6-8M22 10l-6-8" stroke="#888" stroke-width="2"/><path d="M10 13v8M15 13v8M20 13v8" stroke="#888" stroke-width="1.6"/></svg>
    My Cart
  </div>
  <div class="abs cart-info">(0) items<br>0 Recent Items<br>Total - $00.00</div>
  <div class="abs currency"><span class="flag"></span>USD<span class="caret"></span></div>
</div>

<div class="abs navband"></div>
<nav class="abs nav">
  <a class="active" style="width:85px">HOME</a>
  <a style="width:105px">DESIGNS</a>
  <a style="width:97px">CREATE</a>
  <a style="width:90px">ABOUT</a>
  <a style="width:110px">CONTACT</a>
  <a style="width:137px">TESTIMONIALS</a>
  <a style="width:159px;border-right:0">REQUEST A QUOTE</a>
</nav>

<div class="abs slider"></div>
<div class="abs slide-photo" role="img" aria-label="Black zip tablet case opened to show a tablet inside"></div>
<div class="abs slide-panel"></div>
<div class="abs slide-title">Tablet cases</div>
<p class="abs slide-text">Maecenas tristique imperdiet hendrerit. Morbi mauris eros, blandit vel frin-gilla sit amet, gravida sit amet odio. Suspendisse id lacus sed erat hen drerit tempor at id semaccumsan tellus vel.</p>
<div class="abs dark-btn" style="left:358px;top:314px;width:101px">BUY NOW<span class="chev"></span></div>
<div class="abs dark-btn" style="left:464px;top:314px;width:110px">VIEW MORE<span class="chev"></span></div>
<div class="abs price-badge"><span class="just">Just</span><span class="amt">$45</span></div>
<span class="abs dot on" style="left:750px"></span>
<span class="abs dot" style="left:775px"></span>
<span class="abs dot" style="left:799px"></span>
<span class="abs dot" style="left:823px"></span>

<div class="abs section-head" style="left:69px;top:441px;width:539px">OUR PRODUCTS<span class="go"></span></div>

<div class="abs product" style="left:79px">
  <div class="shot"><i role="img" aria-label="Purple flip phone cases"></i></div>
  <div class="name">Nova Grand S3<br>Decorate</div>
  <div class="price" style="top:160px">Price : <b>$00.00</b></div>
  <div class="cart-btn"><svg width="16" height="14" viewBox="0 0 16 14"><path d="M1 1h3l2 8h8l1-6H5" fill="none" stroke="#fff" stroke-width="1.6"/><circle cx="7" cy="12" r="1.3" fill="#fff"/><circle cx="13" cy="12" r="1.3" fill="#fff"/></svg>ADD TO CART</div>
</div>
<div class="abs product" style="left:258px">
  <div class="shot"><i role="img" aria-label="Black leather holster phone case"></i></div>
  <div class="name">Orbit 4 - Decorate</div>
  <div class="price" style="top:144px">Price : <b>$00.00</b></div>
  <div class="cart-btn"><svg width="16" height="14" viewBox="0 0 16 14"><path d="M1 1h3l2 8h8l1-6H5" fill="none" stroke="#fff" stroke-width="1.6"/><circle cx="7" cy="12" r="1.3" fill="#fff"/><circle cx="13" cy="12" r="1.3" fill="#fff"/></svg>ADD TO CART</div>
</div>
<div class="abs product" style="left:438px">
  <div class="shot"><i role="img" aria-label="Black and grey pouch phone cases"></i></div>
  <div class="name">Phone 5 - Decorate</div>
  <div class="price" style="top:144px">Price : <b>$00.00</b></div>
  <div class="cart-btn"><svg width="16" height="14" viewBox="0 0 16 14"><path d="M1 1h3l2 8h8l1-6H5" fill="none" stroke="#fff" stroke-width="1.6"/><circle cx="7" cy="12" r="1.3" fill="#fff"/><circle cx="13" cy="12" r="1.3" fill="#fff"/></svg>ADD TO CART</div>
</div>

<div class="abs section-head" style="left:69px;top:729px;width:539px">CREATE NEW</div>
<p class="abs intro">Praesent et scelerisque arcu. Aenean odio orci, consequat a convallis non, tincidunt in nunc. Pellentesque et facilisis libero. Vestibulum ante ipsum primis in faucibus orci luctus et ultrices posuere cubilia Curae; Sed volutpat nisi ac erat ornare blandit. Aliquam non ligula risus, ac molestie mauris. In sit amet consequat dui. Donec vel massa libero. Nunc sodales, eros quis fringilla eleifend, massa mi tincidunt est, scelerisque auctor arcu nunc sed quam. Donec eu augue diam. Aliquam justo quam, ultricies ut placerat nec.</p>
<div class="abs create-card" style="left:82px"><span class="thumb" role="img" aria-label="Colourful smartphones"></span><span class="label">Create New<br>Smartphone Case</span></div>
<div class="abs create-card" style="left:353px"><span class="thumb" role="img" aria-label="Patterned tablet case" style="background:linear-gradient(135deg,#222,#555 50%,#8a9a7a)"></span><span class="label">Create New<br>Tablet Case</span></div>

<div class="abs section-head" style="left:625px;top:441px;width:227px">DESIGN CATEGORIES</div>
<div class="abs cat-panel">
  <ul class="cat-list">
    <li>Animals</li><li>Arts and Culture</li><li>Building and Environment</li><li>Business</li><li>Celebrations</li><li>Clothing</li><li>Decorative</li><li>Fantasy and Themes</li><li>Food</li><li>Government</li><li>Grunge</li><li>Humor</li><li>Patriot</li><li>People</li><li>Plants</li><li>Religion</li><li>School</li><li>Services</li><li>Sports</li><li>Transportation</li>
  </ul>
</div>

<footer class="abs footer"></footer>
<div class="abs foot-head" style="left:70px;top:993px">Quick Links</div>
<ul class="abs foot-list" style="left:72px;top:1019px"><li>Integer lobortis</li><li>Curabitur ac</li><li>Phasellus tellus nisl</li><li>Aenean fringilla</li><li>Vestibulum</li><li>Aliquam commodo</li></ul>
<ul class="abs foot-list" style="left:209px;top:1019px"><li>Integer lobortis</li><li>Curabitur ac</li><li>Phasellus tellus nisl</li><li>Aenean fringilla</li><li>Vestibulum</li><li>Aliquam commodo</li></ul>
<ul class="abs foot-list" style="left:345px;top:1019px"><li>Integer lobortis</li><li>Curabitur ac</li><li>Phasellus tellus nisl</li><li>Aenean fringilla</li><li>Vestibulum</li><li>Aliquam commodo</li></ul>
<div class="abs vdiv" style="left:461px"></div>
<div class="abs foot-head" style="left:486px;top:993px">Email Signup</div>
<div class="abs field" style="top:1026px">Name</div>
<div class="abs field" style="top:1059px">Email ID</div>
<div class="abs submit">SUBMIT</div>
<div class="abs vdiv" style="left:676px"></div>
<div class="abs foot-head" style="left:694px;top:993px">Connect with us</div>
<div class="abs social" style="top:1027px"><span class="sq"></span>Join with us on <b>Circlespace</b></div>
<div class="abs social" style="top:1059px"><span class="sq" style="background:#2ba9e1"></span>Follow us on <b>Chirpline</b></div>
<div class="abs social" style="top:1091px"><span class="sq" style="background:#1c6fa8"></span>Share on <b>ProNet</b></div>
<div class="abs social" style="top:1123px"><span class="sq" style="background:#c33"></span>Watch on <b>ClipStream</b></div>

<div class="abs copyright">Copyright &copy; 2013 &nbsp; www.brightcasewerk.ca &nbsp; All rights reserved.</div>

</body>
</html>
```